Dental Office Business Card

We need a business card for our pediatric dentistry office.
On one side the design needs to contain the following:
our logo (attached)
Vento Pediatric Grins
Soraya Kadbelani, DDS
Board Certified Pediatric Dentist
Tel: (555) 318-2747)
Fax: (555) 264-8031
Email: info@ventopediatricgrins.example
Web: www.ventopediatricgrins.example
Address: 41 Brindle Ave, Suite 208, Wellesley, MA 02099

On the other side of the card, the design needs to have an appointment reminder (date and time as well as day of the week) similar to the design attached (no need for appointment reason “For”)

```html
<!DOCTYPE html>
<html lang="en">
<head>
<meta charset="utf-8">
<title>Vento Pediatric Grins – Business Card</title>
<link href="https://fonts.googleapis.com/css2?family=Montserrat:ital,wght@0,400;0,500;0,700;1,400&display=swap" rel="stylesheet">
<style>
  :root {
    --bg: #d9d9d9;
    --card: #ffffff;
    --ink: #1c1c1e;
    --ink-soft: #2b2b2b;
    --mint: #a6d9a8;
    --line: #1e2530;
  }
  * { box-sizing: border-box; margin: 0; padding: 0; }
  html, body { width: 1200px; height: 896px; overflow: hidden; }
  body {
    background: var(--bg);
    font-family: "Montserrat", sans-serif;
    color: var(--ink);
    position: relative;
  }
  .card {
    position: absolute;
    left: 334px;
    width: 528px;
    height: 301px;
    background: var(--card);
    border-radius: 20px;
    overflow: hidden;
    box-shadow: 0 10px 22px rgba(0,0,0,0.18);
  }
  .card--front { top: 126px; }
  .card--back { top: 475px; }

  /* Front */
  .brand {
    position: absolute;
    right: 19px;
    top: 22px;
    display: flex;
    align-items: center;
    gap: 10px;
  }
  .brand__dot { width: 44px; height: 44px; border-radius: 50%; background: var(--mint); }
  .brand__name {
    font-weight: 700;
    font-size: 22px;
    line-height: 1.15;
    color: var(--ink);
    text-align: right;
  }
  .dentist { position: absolute; left: 19px; top: 136px; }
  .dentist__accent {
    position: absolute; left: -19px; top: 2px;
    width: 11px; height: 36px; background: var(--mint);
  }
  .dentist__name { font-weight: 700; font-size: 17px; }
  .dentist__title { font-size: 13px; color: var(--ink-soft); margin-top: 3px; letter-spacing: 0.2px; }

  .contacts { position: absolute; left: 24px; top: 203px; list-style: none; }
  .contacts li { display: flex; align-items: center; gap: 6px; font-size: 13.5px; height: 21px; }
  .contacts svg { width: 12px; height: 12px; fill: var(--mint); }

  .office { position: absolute; right: 19px; top: 201px; text-align: right; }
  .office__name { font-weight: 500; font-size: 16.5px; margin-bottom: 5px; }
  .office__addr { font-size: 13.5px; line-height: 21px; }

  .bands { position: absolute; left: 0; bottom: 0; width: 528px; height: 26px; }
  .website {
    position: absolute; right: 19px; bottom: 6px;
    font-size: 12.5px; color: #ffffff; letter-spacing: 0.3px;
  }

  /* Back */
  .reminder__heading { text-align: center; margin-top: 24px; }
  .reminder__title { font-weight: 700; font-size: 23px; letter-spacing: 0.5px; }
  .reminder__sub { font-size: 22px; color: var(--ink-soft); margin-top: 0; }
  .field {
    position: absolute; left: 32px; right: 34px;
    display: flex; align-items: flex-end;
    font-size: 21px; color: var(--ink-soft);
  }
  .field__rule { flex: 1; border-bottom: 1.5px solid var(--line); margin-left: 2px; margin-bottom: 4px; }
  .field--for { top: 100px; }
  .field--date { top: 151px; }
  .days {
    position: absolute; left: 33px; top: 204px; right: 34px;
    display: flex; justify-content: space-between;
    list-style: none; font-style: italic; font-size: 15.5px; color: var(--ink-soft);
  }
  .days li { display: flex; align-items: center; gap: 5px; }
  .days li::before {
    content: ""; width: 15px; height: 15px; border: 1.3px solid var(--ink); display: block;
  }
  .time {
    position: absolute; left: 34px; top: 249px;
    display: flex; align-items: flex-end; font-size: 21px; color: var(--ink-soft);
  }
  .time__rule { width: 130px; border-bottom: 1.5px solid var(--line); margin: 0 15px 6px 2px; }
  .time__period { font-size: 19px; margin-right: 13px; }
</style>
</head>
<body>

<section class="card card--front">
  <div class="brand">
    <span class="brand__dot"></span>
    <span class="brand__name">Vento<br>Pediatric Grins</span>
  </div>

  <div class="dentist">
    <span class="dentist__accent"></span>
    <p class="dentist__name">Soraya Kadbelani, DDS</p>
    <p class="dentist__title">Board Certified Pediatric Dentist</p>
  </div>

  <ul class="contacts">
    <li><svg viewBox="0 0 12 12"><path d="M1 5c0-2 2-3 5-3s5 1 5 3v1H8V5H4v1H1zM2 7h8l1 4H1z"/></svg>(555) 318-2747)</li>
    <li><svg viewBox="0 0 12 12"><path d="M3 1h5v3H3zM1 4h10v8H1zM3 6h2v1H3zm3 0h2v1H6zM3 8h2v1H3zm3 0h2v1H6z"/></svg>(555) 264-8031</li>
    <li><svg viewBox="0 0 12 12"><path d="M0 2h12v1L6 7 0 3zM0 4l6 4 6-4v6H0z"/></svg>info@ventopediatricgrins.example</li>
  </ul>

  <div class="office">
    <p class="office__name">Vento Pediatric Grins</p>
    <p class="office__addr">41 Brindle Ave, Suite<br>208, Wellesley, MA 02099</p>
  </div>

  <svg class="bands" viewBox="0 0 528 26" aria-hidden="true">
    <polygon points="0,16 528,16 528,26 0,26" fill="var(--mint)"/>
    <polygon points="282,0 528,0 528,26 270,26" fill="var(--mint)"/>
    <polygon points="0,4 282,4 276,12 0,12" fill="var(--ink)"/>
  </svg>
  <span class="website">www.ventopediatricgrins.example</span>
</section>

<section class="card card--back">
  <header class="reminder__heading">
    <h1 class="reminder__title">APPOINTMENT</h1>
    <p class="reminder__sub">Reminder</p>
  </header>

  <div class="field field--for">FOR:<span class="field__rule"></span></div>
  <div class="field field--date">DATE:<span class="field__rule"></span></div>

  <ul class="days">
    <li>Mon</li><li>Tue</li><li>Wed</li><li>Thu</li><li>Fri</li><li>Sat</li><li>Sun</li>
  </ul>

  <div class="time">TIME:<span class="time__rule"></span><span class="time__period">A.M.</span><span class="time__period">P.M.</span></div>
</section>

</body>
</html>
```